Design a menu for health restaurant

A health food restaurant in Los Angeles is seeking menu design. Our foods are made from scratch using whole ingredients.
Name: Grubb Larder
Address: 1000 E 60th StLos Angeles, CA 90247
Website: www.GrubbLarder.example
We are looking for a clean and simple menu. Brand colors are white/tan, green and orange.

Please see attached excel with menu items and logo. We do not yet have prices.

Colors
f78f20
9bcb3c
ffffff
fff3d1

Requirements
Must have
• Easy to read.
Trifold menu design (front and back).
VEGAN, VEGETARIAN, GLUTEN FREE, CONTAINS NUTS symbols.
Logo.
Nice to have
• Incorporate brand colors, but still be easy to read.
We would like to use the Belco font (attached) if it works. If not we are open to a similar font that is easy to read.

Please see attached images.
We like the images and headers of OPTION 1. Would like something similar in trifold format.
We like the clean fonts of OPTION 2.

```html
<!DOCTYPE html>
<html lang="en">
<head>
<meta charset="utf-8">
<title>Grubb Larder Menu</title>
<link href="https://fonts.googleapis.com/css2?family=Fredoka:wght@600&family=Didact+Gothic&display=swap" rel="stylesheet">
<style>
:root{
  --bg:#e7e5e1;
  --paper:#f7f7f6;
  --ink:#2b2b2b;
  --muted:#555;
  --orange:#f78f20;
  --logo-orange:#ef5a24;
  --green:#9bcb3c;
  --snacks:#f5cfa0;
  --desserts:#e3a1ab;
  --drinks:#a9cbe6;
  --breakfast:#f0735e;
  --salads:#8ed15a;
  --burgers:#f28a5c;
  --smoothies:#c79ae0;
  --soups:#6fcfab;
  --bowls:#f4a58c;
  --wraps:#c9a566;
  --combos:#f3df8b;
  --rule:#3c7cc0;
}
*{box-sizing:border-box;margin:0;padding:0}
html,body{width:907px;height:1200px;overflow:hidden;background:var(--bg)}
body{position:relative;font-family:"Didact Gothic",sans-serif;color:var(--ink)}
.sheet{position:absolute;background:var(--paper);box-shadow:0 2px 8px rgba(0,0,0,.15);overflow:hidden}
.sheet-front{left:88px;top:20px;width:734px;height:572px}
.sheet-back{left:88px;top:600px;width:744px;height:581px}
.block{position:absolute}
.band{font-family:"Fredoka",sans-serif;font-weight:600;font-size:19px;letter-spacing:.5px;text-transform:uppercase;color:#2a2a2a;padding:4px 0 3px 24px;line-height:1.05}
.list{padding:8px 0 0 24px}
.item{margin-bottom:6px}
.name{font-size:9.5px;line-height:1.2}
.price{font-size:5px;margin-left:3px;vertical-align:middle}
.tag{display:inline-block;width:7px;height:7px;border:.8px solid #444;border-radius:50%;font-size:3.6px;font-style:normal;text-align:center;line-height:6px;margin-left:1px;vertical-align:middle}
.desc{font-size:5.2px;line-height:1.35;color:var(--muted);max-width:124px}
.wide .desc{max-width:150px}
.drinks .desc{max-width:118px}
.bowls .desc{max-width:128px}
.short .desc,.short .name{max-width:112px}
.narrow .name{max-width:132px}
.photo{position:absolute}
.plate{border-radius:50%}
.bottled{position:absolute;left:260px;top:306px;width:212px;height:59px;border:1px solid var(--rule);padding:4px 8px}
.bottled h3{font-weight:normal;font-size:8px;margin-bottom:3px}
.bottled p{font-size:5px;line-height:1.4;color:var(--muted)}
.contact{position:absolute;left:262px;top:402px;width:200px;text-align:center}
.contact h2{font-family:"Fredoka",sans-serif;font-weight:600;font-size:14px;letter-spacing:.6px;border-bottom:1px solid #777;padding-bottom:3px;margin-bottom:8px}
.contact p{font-size:8px;line-height:1.55}
.legend{position:absolute;left:264px;top:520px;width:208px;border-top:1px solid #777;padding-top:6px;display:flex;justify-content:space-between}
.legend span{display:flex;align-items:center;font-size:5.5px;gap:3px;line-height:1.1}
.legend b{display:inline-block;width:14px;height:14px;border:1px solid #333;border-radius:50%;font-size:5px;text-align:center;line-height:12px;font-weight:normal}
.brand{position:absolute;left:542px;top:300px;width:150px;text-align:center}
.brand-mark{width:108px;height:108px;border-radius:50%;background:var(--logo-orange);margin:0 auto 6px}
.brand-name{font-family:"Didact Gothic",sans-serif;font-size:17px;color:var(--logo-orange);letter-spacing:.5px}
.cover{position:absolute;left:533px;top:455px;width:170px;text-align:center}
.cover h1{font-family:"Fredoka",sans-serif;font-weight:600;font-size:22px;letter-spacing:2px;border-bottom:1px solid #777;padding-bottom:6px;margin-bottom:6px}
.cover p{font-size:8px;line-height:1.55}
.cover hr{border:0;border-top:1px solid #777;margin-top:6px}
.intro{font-size:5.3px;font-style:italic;color:var(--muted);max-width:210px;margin-bottom:6px;line-height:1.35}
</style>
</head>
<body>

<section class="sheet sheet-front">
  <div class="photo plate" role="img" aria-label="Beet and greens salad on a white plate" style="left:478px;top:-10px;width:320px;height:320px;background:radial-gradient(circle at 50% 50%,#7a2a45 0,#5f8a3a 35%,#eef0ee 62%,#ffffff 70%)"></div>

  <div class="block" style="left:0;top:20px;width:245px">
    <h2 class="band" style="background:var(--snacks)">Snacks N' Sides</h2>
    <div class="list">
      <div class="item"><div class="name">Fries<span class="price">11.99</span> <i class="tag">GF</i><i class="tag">VG</i></div><div class="desc">Hand cut air-fries with house seasonings. Choose regular or sweet potato fries.</div></div>
      <div class="item"><div class="name">Side Salad<span class="price">11.99</span></div><div class="desc">Your choice of House, Golden Beet, Mediterranean, or Vegan Chef side salad. (20oz)</div></div>
      <div class="item"><div class="name">Guac + Chips<span class="price">11.99</span> <i class="tag">GF</i><i class="tag">VG</i></div><div class="desc">Guacamole with blue corn tortilla chips.</div></div>
      <div class="item"><div class="name">Hummus + Chips<span class="price">11.99</span> <i class="tag">GF</i><i class="tag">VG</i></div><div class="desc">Hummus with blue corn tortilla chips.</div></div>
    </div>
  </div>
  <div class="photo plate" role="img" aria-label="Bowl of hummus with chips" style="left:156px;top:60px;width:76px;height:76px;background:radial-gradient(circle,#e2b04a 0,#c9a06a 40%,#f1e9e4 70%)"></div>
  <div class="photo" role="img" aria-label="Fries with dipping sauce" style="left:52px;top:190px;width:145px;height:90px;border-radius:40%;background:radial-gradient(ellipse,#f0b862 0,#e9c98e 50%,rgba(247,247,246,0) 75%)"></div>

  <div class="block" style="left:0;top:300px;width:245px">
    <h2 class="band" style="background:var(--desserts)">Desserts</h2>
    <div class="list">
      <div class="item"><div class="name">Date Coffee Cake<span class="price">11.99</span> <i class="tag">N</i><i class="tag">V</i></div><div class="desc">Signature date coffee cake with walnuts.</div></div>
      <div class="item"><div class="name">Fruit + Spices<span class="price">11.99</span> <i class="tag">GF</i><i class="tag">VG</i></div><div class="desc">Strawberry, pineapple, green apple, orange, and blueberries with lime and chili seasoning.</div></div>
      <div class="item"><div class="name">Cookies<span class="price">11.99</span> <i class="tag">V</i></div><div class="desc">Your choice of Chocolate Chip or Double Chocolate Chip fresh baked cookie.</div></div>
      <div class="item"><div class="name">Larder Chocolate Mousse<span class="price">11.99</span> <i class="tag">GF</i><i class="tag">VG</i></div><div class="desc">Served with grated dark chocolate.</div></div>
    </div>
  </div>
  <div class="photo" role="img" aria-label="Stacked chocolate chip cookies" style="left:168px;top:330px;width:66px;height:90px;border-radius:30%;background:radial-gradient(ellipse,#9a6a40 0,#b88a5c 45%,rgba(247,247,246,0) 72%)"></div>
  <div class="photo plate" role="img" aria-label="Fruit plate with spoon" style="left:0;top:472px;width:105px;height:105px;background:radial-gradient(circle,#e8703a 0,#d9a070 40%,#f0ece8 68%)"></div>
  <div class="photo" role="img" aria-label="Slice of coffee cake on a plate" style="left:152px;top:472px;width:80px;height:55px;border-radius:50%;background:radial-gradient(ellipse,#a0744a 0,#c79b72 45%,#eceae8 70%)"></div>

  <div class="block drinks" style="left:245px;top:20px;width:245px">
    <h2 class="band" style="background:var(--drinks)">Drinks</h2>
    <div class="list">
      <div class="item"><div class="name">Coffee<span class="price">11.99</span></div><div class="desc">We proudly serve Harbor Lane Coffee, a local roaster.</div></div>
      <div class="item"><div class="name">Power Date Shake<span class="price">11.99</span></div><div class="desc">Ice-blended energy smoothie featuring dates and coffee.</div></div>
      <div class="item"><div class="name">Heart Beet Juice<span class="price">11.99</span> <i class="tag">GF</i><i class="tag">VG</i></div><div class="desc">Red beet, apple, carrot, ginger, parsley, and lemon.</div></div>
      <div class="item"><div class="name">Green Leafy Juice<span class="price">11.99</span> <i class="tag">GF</i><i class="tag">VG</i></div><div class="desc">Spinach, kale, cucumber, apple, and oranges.</div></div>
      <div class="item"><div class="name">Orange Turmeric Juice<span class="price">11.99</span> <i class="tag">GF</i></div><div class="desc">Turmeric, ginger, lemon, carrot, and orange topped with cracked black pepper.</div></div>
      <div class="item"><div class="name">Fireshot<span class="price">11.99</span> <i class="tag">GF</i><i class="tag">VG</i></div><div class="desc">Ginger and lemon shot topped with cayenne.</div></div>
      <div class="item"><div class="name">Lemonade<span class="price">11.99</span> <i class="tag">GF</i></div><div class="desc">House Made Lemonade. Choice of unsweetened or agave sweetened in Regular, Raspberry, and Lavender flavors.</div></div>
      <div class="item"><div class="name">Tea<span class="price">11.99</span></div><div class="desc">Hot or iced.</div></div>
    </div>
  </div>
  <div class="photo" role="img" aria-label="Glasses of red and orange juice" style="left:400px;top:45px;width:62px;height:215px;border-radius:31px;background:linear-gradient(180deg,rgba(247,247,246,0) 0,#e0405a 25%,#f2a93a 55%,#f5c24a 80%,rgba(247,247,246,0) 100%);opacity:.75"></div>

  <div class="bottled">
    <h3>Bottled Drinks <span class="price">11.99</span></h3>
    <p>Brightleaf Kombucha (Trilogy, Gingerberry, Mango)<br>Fizzwell (Orange Mango, Lemon, Grapefruit)<br>Palm Grove Coconut Water<br>Sparkling Water (Clearspring)<br>Still Water (Clearspring)</p>
  </div>

  <div class="contact">
    <h2>CONTACT US</h2>
    <p>
      <svg width="7" height="7" viewBox="0 0 10 10"><circle cx="5" cy="5" r="4" fill="none" stroke="#333"/><path d="M1 5h8M5 1v8" stroke="#333"/></svg> www.GrubbLarder.example<br>
      <svg width="7" height="7" viewBox="0 0 10 10"><path d="M2 1l2 0 1 3-1.5 1a6 6 0 0 0 2.5 2.5L7 6l3 1v2c-5 0-9-4-9-9z" fill="#333"/></svg> 818.555.0142<br>
      <svg width="8" height="6" viewBox="0 0 10 7"><rect x=".5" y=".5" width="9" height="6" fill="#333"/><path d="M.5 .5L5 4 9.5 .5" stroke="#fff" fill="none"/></svg> info@grubblarder.example<br>
      <svg width="6" height="8" viewBox="0 0 10 13"><path d="M5 0a5 5 0 0 1 5 5c0 4-5 8-5 8S0 9 0 5a5 5 0 0 1 5-5z" fill="#333"/><circle cx="5" cy="5" r="2" fill="#fff"/></svg> 2417 W 83rd Street, Los Angeles, CA<br>
      <svg width="6" height="6" viewBox="0 0 10 10"><rect width="10" height="10" fill="#333"/></svg> grubblarder &nbsp;
      <svg width="6" height="6" viewBox="0 0 10 10"><rect width="10" height="10" rx="3" fill="#333"/></svg> @grubblarder
    </p>
  </div>

  <div class="legend">
    <span><b>N</b>Contains<br>Nuts</span>
    <span><b>VG</b>Vegan</span>
    <span><b>GF</b>Gluten<br>Free</span>
    <span><b>V</b>Vegetarian</span>
  </div>

  <div class="brand">
    <div class="brand-mark"></div>
    <div class="brand-name">Grubb Larder</div>
  </div>

  <div class="cover">
    <h1>MENU</h1>
    <p>www.GrubbLarder.example<br>818.555.0142<br>2417 W 83rd Street, Los Angeles, CA</p>
    <hr>
  </div>
</section>

<section class="sheet sheet-back">
  <div class="block" style="left:0;top:21px;width:246px">
    <h2 class="band" style="background:var(--breakfast)">Breakfast</h2>
    <div class="list">
      <div class="item"><div class="name">Pastries<span class="price">11.99</span> <i class="tag">V</i></div><div class="desc">Croissant (regular, almond, chocolate)<br>Blueberry Muffin<br>Superseed Cookie</div></div>
      <div class="item"><div class="name">Parfait<span class="price">11.99</span> <i class="tag">V</i></div><div class="desc">Fresh strawberries and blueberries on yogurt and muesli and topped with honey drizzle.</div></div>
      <div class="item"><div class="name">Avocado Super Toast<span class="price">11.99</span> <i class="tag">VG</i></div><div class="desc">Avocado Mash, Tomato, Basil, Ground Flax, Hemp Seed, Chickpeas, and Moringa Powder on Whole Wheat Bread.</div></div>
      <div class="item"><div class="name">Brunch Burger<span class="price">11.99</span></div><div class="desc">House seasoned beef burger topped with an over medium egg, red leaf lettuce, tomato, housemade pickles and Larder Sauce on a bun.</div></div>
      <div class="item"><div class="name">Breakfast Sandwich<span class="price">11.99</span></div><div class="desc">Your choice of over medium egg or tofu steak with guacamole, tomato, and Larder Sauce on an English muffin.</div></div>
      <div class="item"><div class="name">AM Burrito<span class="price">11.99</span></div><div class="desc">Scrambled eggs, onion, red bell pepper, black beans, housemade salsa, yogurt, and pepper jack cheese in a tortilla.</div></div>
    </div>
  </div>
  <div class="photo plate" role="img" aria-label="Blueberry muffins with coffee" style="left:160px;top:52px;width:84px;height:84px;background:radial-gradient(circle,#d8c7a8 0,#3b3f5a 55%,#2e3550 70%)"></div>

  <div class="block" style="left:0;top:273px;width:246px">
    <h2 class="band" style="background:var(--smoothies)">Smoothies</h2>
    <div class="list">
      <div class="item"><div class="name">Green Machine Smoothie<span class="price">11.99</span> <i class="tag">N</i><i class="tag">GF</i></div><div class="desc">Romaine, spinach, banana, mango, pineapple, flaxmilk, spirulina, almond butter</div></div>
      <div class="item"><div class="name">Acai Smoothie<span class="price">11.99</span> <i class="tag">N</i><i class="tag">GF</i></div><div class="desc">Acai, blueberries, banana, pineapple, Macqui berry, flaxmilk, almond butter</div></div>
      <div class="item"><div class="name">Mango Smoothie<span class="price">11.99</span> <i class="tag">GF</i><i class="tag">VG</i></div><div class="desc">Mango, flaxmilk, banana, hemp seeds</div></div>
    </div>
  </div>
  <div class="photo" role="img" aria-label="Colourful smoothie glasses" style="left:182px;top:300px;width:62px;height:90px;border-radius:40%;background:radial-gradient(ellipse,#b48ad8 0,#e9d2e6 45%,rgba(247,247,246,0) 72%)"></div>

  <div class="block narrow" style="left:0;top:413px;width:246px">
    <h2 class="band" style="background:var(--soups)">Soups</h2>
    <div class="list">
      <div class="item"><div class="name">Chicken Noodle<span class="price">11.99</span></div><div class="desc">Chicken, egg noodles, root vegetables, oregano &amp; peppercorns.</div></div>
      <div class="item"><div class="name">Larder Chili<span class="price">11.99</span> <i class="tag">GF</i></div><div class="desc">Chicken, onions, bell peppers, jalapeños, black &amp; kidney beans, and tomato.</div></div>
      <div class="item"><div class="name">Seasonal Rotating (Butternut Squash Soup)<span class="price">11.99</span></div><div class="desc">Butternut Squash blended with warm spices, and coconut milk.</div></div>
    </div>
  </div>
  <div class="photo plate" role="img" aria-label="Bowl of butternut squash soup" style="left:166px;top:470px;width:78px;height:78px;background:radial-gradient(circle,#f2b22c 0,#f0c451 35%,#efe8dc 62%)"></div>

  <div class="block wide" style="left:246px;top:21px;width:249px">
    <h2 class="band" style="background:var(--salads)">Salads</h2>
    <div class="list">
      <div class="item"><div class="name" style="max-width:150px">Avocado, Golden Beet, and Cranberry Salad<span class="price">11.99</span> <i class="tag">GF</i></div><div class="desc">Gold beets, avocado, dried cranberries, watermelon radish, red kale, romaine, mixed greens, and pepitas served with Golden Buddha dressing</div></div>
      <div class="item short"><div class="name">Burrata Salad<span class="price">11.99</span> <i class="tag">GF</i><i class="tag">V</i></div><div class="desc">Tomato, melon, shredded basil, balsamic glaze, fresh cracked pepper, and olive oil with burrata.</div></div>
      <div class="item short"><div class="name">Mediterranean Salad<span class="price">11.99</span> <i class="tag">GF</i></div><div class="desc">Cucumbers, Kalamata olives, cherry tomatoes, parsley, tricolor quinoa, hard-boiled egg, and hummus on mixed greens, romaine, and red cabbage with lemon-olive oil dressing.</div></div>
      <div class="item short"><div class="name">Vegan Chef Salad<span class="price">11.99</span> <i class="tag">VG</i><i class="tag">GF</i></div><div class="desc">Roasted potatoes and carrots, chickpeas, avocado, microgreens and walnuts on mixed greens, romaine, and red kale with ranch.</div></div>
      <div class="item"><div class="name">Rancher's Salad<span class="price">11.99</span> <i class="tag">GF</i></div><div class="desc">Tomato, red onion, hard boiled egg, avocado, feta cheese, microgreens, and grilled chicken on romaine with Ranch dressing</div></div>
    </div>
  </div>
  <div class="photo plate" role="img" aria-label="Green salad in a white bowl" style="left:398px;top:92px;width:78px;height:78px;background:radial-gradient(circle,#d34a3a 0,#6fa84a 40%,#eef0ea 68%)"></div>

  <div class="block bowls" style="left:246px;top:265px;width:249px">
    <h2 class="band" style="background:var(--bowls)">Bowls</h2>
    <div class="list">
      <p class="intro">Our signature bowls with your choice of roasted chickpeas (+2.49), grilled chicken (+3.49), seared salmon (+6.49), or grilled steak (+7.49)</p>
      <div class="item"><div class="name">Southwest Bowl<span class="price">11.99</span> <i class="tag">GF</i><i class="tag">VG</i></div><div class="desc">Your choice of protein with corn, black beans, red onions, almonds and avocado over quinoa with lime hot sauce.</div></div>
      <div class="item"><div class="name">Chimi Bowl<span class="price">11.99</span> <i class="tag">GF</i></div><div class="desc">Your choice of protein with red bell pepper, mushrooms, zucchini, squash, onion, cherry tomatoes and fresh herb chimichurri on wild and brown rice.</div></div>
      <div class="item"><div class="name">Soba Noodle Bowl<span class="price">11.99</span> <i class="tag">GF</i></div><div class="desc">Your choice of protein with spinach, snow peas, roasted carrots, red bell pepper, cilantro, sesame seeds and ginger lime sauce over soba noodles.</div></div>
      <div class="item"><div class="name">Hollywood Bowl<span class="price">11.99</span> <i class="tag">GF</i></div><div class="desc">Your choice of protein with broccoli, roasted corn, cherry tomatoes, basil, pepitas, flax seeds and lemon juice on wild and brown rice.</div></div>
      <div class="item"><div class="name">Larder Bowl<span class="price">11.99</span> <i class="tag">GF</i></div><div class="desc">Your choice of protein with roasted chickpeas and cauliflower, zesty fennel salad and citrus yogurt.</div></div>
      <div class="item"><div class="name">Buddha Bowl<span class="price">11.99</span> <i class="tag">GF</i></div><div class="desc">Your choice of protein with corn, red kale, sweet potatoes, red cabbage, parsley, oregano, hummus, and taro.</div></div>
      <div class="item"><div class="name">Chili Rice Bowl<span class="price">11.99</span> <i class="tag">GF</i></div><div class="desc">Chicken, onions, bell peppers, jalapeños, black &amp; kidney beans, and tomato over brown rice.</div></div>
    </div>
  </div>
  <div class="photo plate" role="img" aria-label="Grain bowl with vegetables" style="left:412px;top:330px;width:78px;height:78px;background:radial-gradient(circle,#e0a040 0,#5a7a3a 45%,#2d2d2d 68%)"></div>
  <div class="photo plate" role="img" aria-label="Bowl with greens and grains" style="left:412px;top:458px;width:76px;height:76px;background:radial-gradient(circle,#c6a36a 0,#4f8a3c 45%,#efeee9 68%)"></div>

  <div class="block wide" style="left:495px;top:21px;width:249px">
    <h2 class="band" style="background:var(--burgers)">Burgers N'<br>Sandwiches</h2>
    <div class="list" style="padding-top:16px">
      <div class="item"><div class="name">Air Fried Chicken Sandwich<span class="price">11.99</span></div><div class="desc">Air fried chicken breast topped with red leaf lettuce, tomato, house made pickles and Larder Sauce on a bun served with choice of salad of fries.</div></div>
      <div class="item"><div class="name">Grilled Chicken Sandwich<span class="price">11.99</span></div><div class="desc">Grilled chicken topped with guacamole, red leaf lettuce, tomato, house made pickles and Larder Sauce. Served with regular fries or side salad.</div></div>
      <div class="item"><div class="name">Classic Beef Burger<span class="price">11.99</span></div><div class="desc">House seasoned beef burger topped with red leaf lettuce, tomato, cheddar cheese, house made pickles and Larder Sauce on a bun served with choice of salad of fries.</div></div>
      <div class="item"><div class="name">Black Bean Pine Nut Burger<span class="price">11.99</span> <i class="tag">N</i><i class="tag">V</i></div><div class="desc">House made black bean pine nut burger topped with red leaf lettuce, tomato, house made pickles and mustard aioli on a bun served with choice of salad of fries.</div></div>
      <div class="item"><div class="name">Salmon Burger<span class="price">11.99</span></div><div class="desc">House made salmon burger topped with red leaf lettuce, tomato, house made pickles and Larder yogurt on a bun served with choice of salad or fries.</div></div>
    </div>
  </div>
  <div class="photo" role="img" aria-label="Burger with lettuce and tomato" style="left:680px;top:110px;width:64px;height:70px;border-radius:45%;background:radial-gradient(ellipse,#d9492e 0,#e59a3a 40%,rgba(247,247,246,0) 72%)"></div>
  <div class="photo" role="img" aria-label="Stacked sandwich halves" style="left:676px;top:190px;width:68px;height:70px;border-radius:45%;background:radial-gradient(ellipse,#7aa84a 0,#d8b070 40%,rgba(247,247,246,0) 72%)"></div>

  <div class="block wide" style="left:495px;top:276px;width:249px">
    <h2 class="band" style="background:var(--wraps)">Wraps</h2>
    <div class="list">
      <div class="item"><div class="name">Rancher's Wrap<span class="price">11.99</span></div><div class="desc">Tomato, red onion, hard boiled egg, avocado, feta cheese, microgreens, romaine, grilled chicken and Ranch dressing in a grilled wrap.</div></div>
      <div class="item"><div class="name">Vegan Tuna Wrap<span class="price">11.99</span> <i class="tag">VG</i></div><div class="desc">Vegan tuna, romaine, avocado, celery, shallot, and oregano with Herbalicious Sauce in a whole grain wrap.</div></div>
      <div class="item"><div class="name">Vegetarian Wrap<span class="price">11.99</span> <i class="tag">V</i></div><div class="desc">Roasted chickpeas, romaine, avocado, red bell pepper, shaved carrots, cucumber, spinach, basil, black beans and feta with lemon-hummus in a sprouted 7-grain wrap.</div></div>
    </div>
  </div>
  <div class="photo" role="img" aria-label="Wraps cut in half" style="left:680px;top:340px;width:64px;height:80px;border-radius:45%;background:radial-gradient(ellipse,#c8a060 0,#7a9a48 40%,rgba(247,247,246,0) 72%)"></div>

  <div class="block" style="left:495px;top:430px;width:249px">
    <h2 class="band" style="background:var(--combos)">Combos</h2>
    <div class="list">
      <div class="item"><div class="name">Soup + Salad<span class="price">11.99</span></div><div class="desc">Your choice of soup and side salad.<br>16oz soup + 30oz salad</div></div>
      <div class="item"><div class="name">Avo Toast Combo<span class="price">11.99</span></div><div class="desc">Half avocado toast and your choice of soup. 16oz</div></div>
      <div class="item"><div class="name">Soup + Sandwich<span class="price">11.99</span></div><div class="desc">Your choice of soup and sandwich.<br>16oz soup + Sandwich</div></div>
    </div>
  </div>
  <div class="photo plate" role="img" aria-label="Soup and salad bowls" style="left:672px;top:448px;width:72px;height:60px;background:radial-gradient(circle,#e8b340 0,#5d8a3a 45%,rgba(247,247,246,0) 70%)"></div>
  <div class="photo" role="img" aria-label="Avocado toast slices" style="left:664px;top:512px;width:76px;height:60px;border-radius:45%;background:radial-gradient(ellipse,#8dbb4a 0,#c49a62 45%,rgba(247,247,246,0) 72%)"></div>
</section>

</body>
</html>
```